Letterhead Design Project

Attached is our new Logo and a copy of our old letter head
Looking to rebrand with our new logo

Reason: I want to show a business card design

Industry/Entity Type

Film Production

Colors

Designer to choose colors to be used in the design.

Requirements
Must have
• The information on the old letterhead

```html
<!DOCTYPE html>
<html lang="en">
<head>
<meta charset="utf-8">
<title>Varlo International Letterhead</title>
<link href="https://fonts.googleapis.com/css2?family=Arimo:wght@400;700&display=swap" rel="stylesheet">
<style>
  :root {
    --band-blue: #1b93c9;
    --band-orange: #f28c28;
    --brand-blue: #1b84b8;
    --ink: #1a1a1a;
    --paper: #ffffff;
    --venue-red: #c8283a;
    --venue-navy: #2a3f8f;
    --venue-faint: #eef0f5;
  }
  html, body {
    margin: 0;
    padding: 0;
    overflow: hidden;
    background: var(--paper);
  }
  .letterhead {
    position: relative;
    width: 849px;
    height: 1200px;
    overflow: hidden;
    background: var(--paper);
    font-family: "Arimo", Arial, sans-serif;
    color: var(--ink);
  }
  .side-band {
    position: absolute;
    top: 0;
    left: 0;
    width: 53px;
    height: 1200px;
    background: var(--band-blue);
  }
  .side-stripe {
    position: absolute;
    top: 0;
    left: 53px;
    width: 11px;
    height: 1200px;
    background: var(--band-orange);
  }
  .brand-name {
    position: absolute;
    left: 84px;
    top: 84px;
    width: 140px;
    margin: 0;
    font-weight: 700;
    font-size: 22px;
    line-height: 1.2;
    color: var(--brand-blue);
  }
  .brand-name span { display: block; }
  .contact-block {
    position: absolute;
    left: 236px;
    top: 75px;
    width: 420px;
    text-align: center;
    font-size: 11px;
    line-height: 1;
  }
  .contact-block p { margin: 0; white-space: nowrap; }
  .contact-block .tagline { margin-bottom: 16px; }
  .contact-block .addresses { margin-bottom: 13px; }
  .venue-badge {
    position: absolute;
    left: 618px;
    top: 64px;
    width: 152px;
    height: 68px;
    border-radius: 8px;
    background: linear-gradient(180deg, var(--venue-navy) 0%, var(--venue-red) 55%, var(--venue-navy) 100%);
    opacity: 0.85;
  }
  .venue-backdrop {
    position: absolute;
    left: 256px;
    top: 700px;
    width: 593px;
    height: 370px;
    background: linear-gradient(180deg, rgba(238,240,245,0) 0%, var(--venue-faint) 40%, #f7e9ec 70%, rgba(238,240,245,0.6) 100%);
  }
  .footer-block {
    position: absolute;
    left: 150px;
    top: 1090px;
    width: 560px;
    text-align: center;
    font-size: 13px;
    line-height: 1;
  }
  .footer-block p { margin: 0 0 9px; }
  .footer-block .divisions-note { font-size: 10.5px; }
  .footer-block .company-line { font-size: 14px; }
  .footer-block .registry { font-size: 13px; margin-top: 2px; }
</style>
</head>
<body>
<main class="letterhead">
  <div class="side-band"></div>
  <div class="side-stripe"></div>

  <p class="brand-name"><span>Varlo</span><span>International</span></p>

  <header class="contact-block">
    <p class="tagline">Supply &amp; Management of Infrastructure &amp; Logistics</p>
    <p class="addresses">P.O. Box 312 Riverbend QLD 4305&nbsp;&nbsp;&nbsp;P.O.Box 418 Ashgrove NSW 2175</p>
    <p class="phone-email">Ph. 0400 555 018&nbsp;&nbsp;&nbsp;Email. hello@varlo.com.au</p>
  </header>

  <div class="venue-badge" role="img" aria-label="Small illustration of a striped event marquee with flags"></div>

  <div class="venue-backdrop" role="img" aria-label="Faint large illustration of a striped event marquee with flag poles"></div>

  <footer class="footer-block">
    <p class="divisions">♦ VARLO Film Services&nbsp; ♦&nbsp; VARLO Pilot Escorts ♦ VARLO Tour Management ♦</p>
    <p class="divisions">♦ VARLO Driver ♦</p>
    <p class="company-line"><span class="divisions-note">are divisions of</span> Varlo International Pty Ltd</p>
    <p class="registry">ACN 000 482 716&nbsp; ABN 00 000 482 716</p>
  </footer>
</main>
</body>
</html>
```